Western Canadian Survey Company needs Business Card and Letter Head Design

Hello,

We're looking to have our business cards redesigned along with our letterhead.

We've recently changed out logo and would like to use this. Please use some creativity and propose different options (Traditional and modern).

We will provide as much feedback as possible.

Business card should be double sided with our logo. We would also like room for cell phone number, email address and position. Back of the card can just be our logo or potentially a list of our services we provide.

Industry/Entity Type

Business

Contact Information for Business Card

```html
<!DOCTYPE html>
<html lang="en">
<head>
<meta charset="utf-8">
<title>Ridgeline Field Surveys Ltd – Stationery</title>
<link rel="stylesheet" href="https://fonts.googleapis.com/css2?family=Open+Sans:ital,wght@0,400;0,600;0,700;1,400&display=swap">
<style>
  :root {
    --page-bg: #e6e7e9;
    --ink: #1f2226;
    --ink-soft: #5a5f66;
    --dark: #141517;
    --dark-2: #222428;
    --steel: #4c6b87;
    --steel-deep: #2f4456;
    --steel-pale: #9fb2c3;
    --paper: #ffffff;
  }
  * { box-sizing: border-box; margin: 0; padding: 0; }
  html, body {
    width: 796px; height: 1200px; overflow: hidden;
    background: var(--page-bg);
    font-family: "Open Sans", Arial, sans-serif;
    color: var(--ink);
  }
  .sheet { position: absolute; box-shadow: 0 2px 6px rgba(0,0,0,.12); overflow: hidden; }

  /* wordmark */
  .wordmark { display: flex; align-items: center; gap: 7px; color: var(--steel); }
  .wordmark__mark { width: 14px; height: 14px; background: currentColor; flex: none; }
  .wordmark__name { font-weight: 700; text-transform: uppercase; font-size: 13px; line-height: 1.1; letter-spacing: .5px; }
  .wordmark--light { color: var(--paper); }

  /* footer band shared */
  .band { position: absolute; left: 0; right: 0; }
  .band__bar { position: absolute; left: 0; height: 6px; background: linear-gradient(90deg, var(--steel-deep), var(--steel) 60%, var(--steel-pale)); }
  .band__line { position: absolute; left: 0; right: 0; height: 1px; background: var(--steel); }
  .band__web { position: absolute; right: 14px; font-style: italic; font-size: 10px; color: var(--ink); }

  /* card back */
  .card-back { left: 40px; top: 90px; width: 350px; height: 200px; background: linear-gradient(135deg, var(--dark-2), var(--dark)); display: flex; align-items: center; justify-content: center; }
  .card-back .wordmark__name { font-size: 15px; }

  /* card front */
  .card-front { left: 406px; top: 90px; width: 350px; height: 200px; background: var(--paper); }
  .card-front .wordmark { position: absolute; right: 20px; top: 34px; }
  .person__name { position: absolute; left: 24px; top: 46px; font-size: 17px; font-weight: 600; line-height: 1.2; }
  .person__role { position: absolute; left: 24px; top: 68px; font-size: 12px; line-height: 1.2; color: var(--steel); }
  .contact { position: absolute; left: 24px; top: 94px; list-style: none; font-size: 10px; line-height: 1.35; color: var(--ink); }
  .contact li { display: flex; gap: 8px; margin-bottom: 4px; }
  .contact svg { width: 9px; height: 9px; flex: none; margin-top: 2px; fill: var(--steel-deep); }
  .card-front .band { top: 170px; height: 30px; }
  .card-front .band__bar { width: 230px; top: 0; }
  .card-front .band__line { top: 7px; }
  .card-front .band__web { top: 11px; }

  /* letterhead */
  .letterhead { left: 40px; top: 330px; width: 500px; height: 707px; background: var(--paper); }
  .letterhead .wordmark { position: absolute; left: 44px; top: 40px; }
  .sender { position: absolute; right: 44px; top: 100px; width: 130px; font-size: 7.5px; line-height: 1.6; color: var(--ink-soft); }
  .sender strong { display: block; color: var(--ink); font-size: 9px; font-weight: 600; }
  .letter { position: absolute; left: 44px; top: 180px; width: 412px; font-size: 8.5px; line-height: 1.75; color: var(--ink-soft); }
  .letter p { margin-bottom: 11px; text-align: justify; }
  .letterhead .band { top: 660px; height: 47px; }
  .letterhead .band__bar { width: 340px; top: 0; }
  .letterhead .band__line { top: 8px; }
  .letterhead .band__web { top: 14px; right: 24px; }

  /* envelope front */
  .envelope-front { left: 566px; top: 330px; width: 190px; height: 100px; background: var(--paper); }
  .envelope-front .wordmark { position: absolute; left: 12px; top: 12px; }
  .envelope-front .wordmark__mark { width: 8px; height: 8px; }
  .envelope-front .wordmark__name { font-size: 7px; }
  .envelope-front .contact { left: 12px; top: 40px; font-size: 5px; }
  .envelope-front .contact li { gap: 4px; margin-bottom: 1px; }
  .envelope-front .contact svg { width: 5px; height: 5px; margin-top: 1px; }
  .envelope-front .band { top: 86px; height: 14px; }
  .envelope-front .band__bar { width: 110px; height: 3px; top: 0; }
  .envelope-front .band__line { top: 4px; }
  .envelope-front .band__web { top: 5px; right: 8px; font-size: 5px; }

  /* folder cover */
  .folder { left: 566px; top: 450px; width: 190px; height: 264px; background: linear-gradient(160deg, var(--dark-2), var(--dark)); display: flex; align-items: center; justify-content: center; }
  .folder .wordmark__mark { width: 10px; height: 10px; }
  .folder .wordmark__name { font-size: 9px; }

  /* envelope back */
  .envelope-back { left: 566px; top: 734px; width: 190px; height: 100px; background: var(--paper); }
  .envelope-back svg.flap { position: absolute; left: 0; top: 0; width: 190px; height: 100px; }
  .envelope-back .wordmark { position: absolute; left: 0; right: 0; top: 18px; justify-content: center; }
  .envelope-back .wordmark__mark { width: 7px; height: 7px; }
  .envelope-back .wordmark__name { font-size: 6px; }
</style>
</head>
<body>

  <section class="sheet card-back">
    <div class="wordmark wordmark--light">
      <span class="wordmark__mark"></span>
      <span class="wordmark__name">Ridgeline Field<br>Surveys Ltd</span>
    </div>
  </section>

  <section class="sheet card-front">
    <div class="wordmark">
      <span class="wordmark__mark"></span>
      <span class="wordmark__name">Ridgeline Field<br>Surveys Ltd</span>
    </div>
    <div class="person__name">Daniel Hart</div>
    <div class="person__role">Manager</div>
    <ul class="contact">
      <li><svg viewBox="0 0 10 10"><path d="M5 0a3.5 3.5 0 0 0-3.5 3.5C1.5 6 5 10 5 10s3.5-4 3.5-6.5A3.5 3.5 0 0 0 5 0zm0 5a1.5 1.5 0 1 1 0-3 1.5 1.5 0 0 1 0 3z"/></svg><span>418 Cedar Ridge Road<br>Vernon, BC. V1T 4K2</span></li>
      <li><svg viewBox="0 0 10 10"><path d="M0 2h10v6H0zM0 2l5 3.5L10 2" stroke="#fff" stroke-width=".8"/></svg><span>office@ridgelinesurveys.net</span></li>
      <li><svg viewBox="0 0 10 10"><path d="M2 0h2l1 2.5-1.3 1a6 6 0 0 0 2.8 2.8l1-1.3L10 6v2a2 2 0 0 1-2 2A8 8 0 0 1 0 2a2 2 0 0 1 2-2z"/></svg><span>+780 555 0142</span></li>
    </ul>
    <div class="band">
      <div class="band__bar"></div>
      <div class="band__line"></div>
      <div class="band__web">www.ridgelinesurveys.ca</div>
    </div>
  </section>

  <section class="sheet letterhead">
    <div class="wordmark">
      <span class="wordmark__mark"></span>
      <span class="wordmark__name">Ridgeline Field<br>Surveys Ltd</span>
    </div>
    <div class="sender">
      <strong>Daniel Hart</strong>
      418 Cedar Ridge Road<br>Vernon, BC. V1T 4K2<br>office@ridgelinesurveys.net<br>+780 555 0142
    </div>
    <div class="letter">
      <p>Dear Client,</p>
      <p>Thank you for choosing our team for your upcoming project. We have reviewed the site plans and prepared a schedule for the initial field survey and layout work.</p>
      <p>Our crew will arrive on the agreed date with all equipment needed to set control points, confirm boundaries and record existing features. A summary report will follow within five business days.</p>
      <p>Our field staff follow strict safety procedures on every site. We coordinate with your project manager before arrival and keep the work area clear of hazards at all times.</p>
      <p>All survey data is checked by a licensed surveyor before release. Digital files can be delivered in the format your design team prefers, along with signed plans where required.</p>
      <p>Please contact our office if you have any questions or need to adjust the timeline. We look forward to working with you.</p>
      <p>Sincerely,<br>Daniel Hart</p>
    </div>
    <div class="band">
      <div class="band__bar"></div>
      <div class="band__line"></div>
      <div class="band__web">www.ridgelinesurveys.ca</div>
    </div>
  </section>

  <section class="sheet envelope-front">
    <div class="wordmark">
      <span class="wordmark__mark"></span>
      <span class="wordmark__name">Ridgeline Field<br>Surveys Ltd</span>
    </div>
    <ul class="contact">
      <li><svg viewBox="0 0 10 10"><path d="M5 0a3.5 3.5 0 0 0-3.5 3.5C1.5 6 5 10 5 10s3.5-4 3.5-6.5A3.5 3.5 0 0 0 5 0z"/></svg><span>418 Cedar Ridge Road, Vernon, BC. V1T 4K2</span></li>
      <li><svg viewBox="0 0 10 10"><path d="M0 2h10v6H0z"/></svg><span>office@ridgelinesurveys.net</span></li>
      <li><svg viewBox="0 0 10 10"><path d="M2 0h2l1 2.5-1.3 1a6 6 0 0 0 2.8 2.8l1-1.3L10 6v2a2 2 0 0 1-2 2A8 8 0 0 1 0 2a2 2 0 0 1 2-2z"/></svg><span>+780 555 0142</span></li>
    </ul>
    <div class="band">
      <div class="band__bar"></div>
      <div class="band__line"></div>
      <div class="band__web">www.ridgelinesurveys.ca</div>
    </div>
  </section>

  <section class="sheet folder">
    <div class="wordmark wordmark--light">
      <span class="wordmark__mark"></span>
      <span class="wordmark__name">Ridgeline Field<br>Surveys Ltd</span>
    </div>
  </section>

  <section class="sheet envelope-back">
    <svg class="flap" viewBox="0 0 190 100" aria-hidden="true">
      <path d="M0 0H190V34Q95 62 0 34Z" fill="#141517"/>
      <path d="M0 38Q95 66 190 38" fill="none" stroke="#4c6b87" stroke-width="2"/>
    </svg>
    <div class="wordmark wordmark--light">
      <span class="wordmark__mark"></span>
      <span class="wordmark__name">Ridgeline Field Surveys Ltd</span>
    </div>
  </section>

</body>
</html>
```